vascular clinic webdesign (wordpress+neve theme+ elementor)

Create a nice webdesign for an existing website of a vascular surgery clinic. Vascular surgery is the medical specialty that treats arteries and veins. Content should not change. First landing page we can recreate content if needed, but internal pages should not change content. We currently use Neve theme (https://plumecraft.net/skins/orla/) in a Wordpress CMS, which is highly customizable, we prefer to keep using it, as it is standard in all our sites, and will be often upgraded. We also have Elementor Pro. Please visit current domain: lumeria.net.
Page is in portuguese. But you can do anything in English that I translate later, or you can use original domain content already in portuguese.
Selected design need to be coded in wordpress+neve+elementor

Minimum pages:
First Page/Landing page (https://lumeria.net/)
Contact page (https://lumeria.net/contato/)
Post/Article page
About us (https://lumeria.net/a-clinica/)
Posts Archive (https://lumeria.net/todos-artigos/)
The team (https://lumeria.net/sobre-nos-equipe-de-cirurgia-vascular-endovascular-ecografia-angiologia/)

Target Market(s)

mostly (70%) woman, 30 to 60 years

Industry/Entity Type

Health

Coding

Coded - Design and coding required

Number of Pages Required

5+ page

Font styles to use
Serif

Requirements
Should not have
• Will not change Wordpress for any other CMS
Prefer not to change theme Neve (https://plumecraft.net/skins/orla/)

```html
<!DOCTYPE html>
<html lang="pt">
<head>
<meta charset="utf-8">
<title>Todos artigos · Lumeria.net</title>
<link href="https://fonts.googleapis.com/css2?family=Playfair+Display:wght@700&family=Poppins:wght@400;500;600&display=swap" rel="stylesheet">
<style>
:root{
  --navy:#0b5a8c;
  --wine:#8a2a22;
  --wine-dark:#6e1c16;
  --ink:#222;
  --muted:#555;
  --footer:#232323;
  --white:#fff;
  --soft:#eef0f2;
}
*{box-sizing:border-box;margin:0;padding:0}
html,body{width:667px;height:1200px;overflow:hidden;background:var(--white);font-family:'Poppins',sans-serif;color:var(--ink)}
.page{position:relative;width:667px;height:1200px}
.site-header{position:absolute;top:0;left:0;width:667px;height:38px;background:var(--white);z-index:3;display:flex;align-items:center;justify-content:space-between;padding:0 50px}
.brand{font-family:'Playfair Display',serif;font-size:15px;color:var(--navy);letter-spacing:.5px}
.main-nav{display:flex;gap:17px;font-size:8px;font-weight:500}
.main-nav a{color:var(--ink);text-decoration:none}
.hero{position:absolute;top:38px;left:0;width:667px;height:200px}
.hero-photo{position:absolute;inset:0;background:linear-gradient(120deg,#4c5a3c 0%,#6b7a55 35%,#8d8a7a 60%,#b7aaa0 80%,#7f8a72 100%)}
.hero-wave{position:absolute;left:0;top:0}
.hero h1{position:absolute;top:48px;width:100%;text-align:center;font-family:'Playfair Display',serif;font-size:30px;color:var(--white)}
.card{position:absolute;width:183px;height:218px;background:var(--white);border-radius:8px;box-shadow:0 2px 8px rgba(0,0,0,.1);overflow:hidden}
.card .thumb{height:124px}
.card .body{padding:15px 18px 0}
.card h2{font-size:8.5px;font-weight:600;line-height:1.2;margin-bottom:3px}
.card .meta{font-size:6px;color:var(--muted);margin-bottom:3px}
.card p{font-size:6.8px;line-height:1.45;color:var(--muted);height:30px;overflow:hidden}
.card .more{display:block;margin-top:5px;font-size:6.8px;font-weight:500;color:var(--wine);text-decoration:none}
.pager{position:absolute;top:743px;left:246px;display:flex;align-items:center;gap:9px;font-size:6px}
.pager .prev{background:var(--soft);border-radius:9px;padding:4px 11px;color:var(--muted)}
.pager .cur{width:17px;height:17px;border-radius:50%;background:var(--wine);color:#fff;display:flex;align-items:center;justify-content:center}
.pager .next{background:var(--navy);border-radius:9px;padding:4px 12px;color:#fff;font-weight:600;margin-left:6px}
.cta{position:absolute;top:780px;left:0;width:667px;height:250px}
.cta h2{position:absolute;top:92px;width:100%;text-align:center;font-family:'Playfair Display',serif;font-size:23px;color:var(--white)}
.cta .btn{position:absolute;top:112px;left:268px;width:132px;height:17px;margin-top:18px;background:#fff;border-radius:9px;text-align:center;font-size:7px;font-weight:600;line-height:17px;color:var(--ink);letter-spacing:.3px}
.site-footer{position:absolute;top:1030px;left:0;width:667px;height:170px;background:var(--footer);color:#cfcfcf}
.f-brand{position:absolute;top:38px;left:49px;font-family:'Playfair Display',serif;font-size:17px;color:#fff;letter-spacing:.5px}
.f-about{position:absolute;top:60px;left:49px;width:192px;font-size:6.6px;line-height:1.55}
.f-col{position:absolute;top:34px}
.f-col h3{font-family:'Playfair Display',serif;font-size:10px;color:#fff;margin-bottom:6px}
.f-col a{display:block;font-size:6.8px;color:#cfcfcf;text-decoration:none;line-height:14px}
.social{position:absolute;top:63px;left:496px;display:flex;gap:4px}
.social span{width:19px;height:19px;border-radius:50%;background:#383838}
.to-top{position:absolute;top:138px;left:630px;width:17px;height:17px;border-radius:50%;background:#b52a22}
.f-rule{position:absolute;top:146px;left:49px;width:569px;height:1px;background:#444}
.copy{position:absolute;top:155px;width:100%;text-align:center;font-size:6.8px;color:#ddd}
</style>
</head>
<body>
<div class="page">
  <header class="site-header">
    <span class="brand">LUMERIA.NET</span>
    <nav class="main-nav">
      <a href="https://lumeria.net/a-clinica/">A Clínica</a>
      <a href="https://lumeria.net/sobre-nos-equipe-de-cirurgia-vascular-endovascular-ecografia-angiologia/">A Equipe</a>
      <a href="#">Problemas Vasculares</a>
      <a href="#">Soluções</a>
      <a href="https://lumeria.net/contato/">Contato</a>
    </nav>
  </header>

  <section class="hero">
    <div class="hero-photo" role="img" aria-label="Vista aérea da clínica cercada por árvores e rua"></div>
    <svg class="hero-wave" width="667" height="200" viewBox="0 0 667 200">
      <path d="M0 175 C150 135 320 120 440 122 C480 123 470 160 478 180 C488 205 520 198 560 180 C610 155 640 135 667 110 L667 200 L0 200 Z" fill="#fff"/>
      <path d="M0 175 C150 135 320 120 440 122 C480 123 470 160 478 180 C488 205 520 198 560 180 C610 155 640 135 667 110" fill="none" stroke="#0b5a8c" stroke-width="5"/>
    </svg>
    <h1>Todos artigos</h1>
  </section>

  <article class="card" style="top:269px;left:48px">
    <div class="thumb" role="img" aria-label="Potes de iogurte com mirtilos e framboesas" style="background:linear-gradient(135deg,#f2f2f4,#e4e6ea 60%,#d9b0b5)"></div>
    <div class="body"><h2>Probiotics</h2><div class="meta">January 15, 2021 &nbsp;No Comments</div><p>Os probioticos estão sendo cada vez mais utilizados na medicina. Os probióticos são bactérias vivas, chamadas de …</p><a class="more" href="#">READ MORE</a></div>
  </article>
  <article class="card" style="top:269px;left:240px">
    <div class="thumb" role="img" aria-label="Pés descalços sobre piso claro" style="background:linear-gradient(135deg,#eef0f5,#dfe3ea 50%,#e8d4c8)"></div>
    <div class="body"><h2>What is Godet's sign?</h2><div class="meta">January 15, 2021 &nbsp;No Comments</div><p>Have you heard of Godet's sign? Although the name is somewhat unknown, the Godet sign is a fairly common tactic when</p><a class="more" href="#">READ MORE</a></div>
  </article>
  <article class="card" style="top:269px;left:433px">
    <div class="thumb" role="img" aria-label="Pessoa segurando tábua com alimentos mediterrâneos" style="background:linear-gradient(135deg,#5b4a40,#8a6a50 50%,#3d4a5c)"></div>
    <div class="body"><h2>How to make the Mediterra...</h2><div class="meta">January 15, 2021 &nbsp;No Comments</div><p>The Mediterranean diet, also known as the Mediterranean diet, is more than just a menu to follow for a few days. It's a lifestyle</p><a class="more" href="#">READ MORE</a></div>
  </article>

  <article class="card" style="top:500px;left:48px">
    <div class="thumb" role="img" aria-label="Balança de vidro com fita métrica" style="background:linear-gradient(135deg,#f6f6f6,#e6ece8 50%,#cde0ee)"></div>
    <div class="body"><h2>Do you need to lose weight to operate on varicose veins?</h2><div class="meta">January 15, 2021 &nbsp;No Comments</div><p>Você já ouviu falar que para operar as varizes é obrigatório emagrecer? Algumas …</p><a class="more" href="#">READ MORE</a></div>
  </article>
  <article class="card" style="top:500px;left:240px">
    <div class="thumb" role="img" aria-label="Pernas subindo escada de pedra" style="background:linear-gradient(135deg,#6a6a66,#8c847a 50%,#4f4d4a)"></div>
    <div class="body"><h2>List of signs and symptoms of lipedema</h2><div class="meta">January 15, 2021 &nbsp;No Comments</div><p>A lipedema is a symmetrical increase in fat, usually occurs in the legs, buttocks…</p><a class="more" href="#">READ MORE</a></div>
  </article>
  <article class="card" style="top:500px;left:433px">
    <div class="thumb" role="img" aria-label="Médica examinando perna com varizes" style="background:linear-gradient(135deg,#eef0f2,#e2d5cc 55%,#d7b3a6)"></div>
    <div class="body"><h2>Confira 5 tipos de tratamentos de varizes</h2><div class="meta">January 15, 2021 &nbsp;No Comments</div><p>As varizes atingem uma parcela considerável do público feminino. Além de…</p><a class="more" href="#">READ MORE</a></div>
  </article>

  <nav class="pager">
    <span class="prev">‹ &nbsp;Prev</span>
    <span style="margin-left:6px">1</span><span class="cur">2</span><span>3</span><span>…</span><span>82</span>
    <span class="next">Next ›</span>
  </nav>

  <section class="cta">
    <svg width="667" height="250" viewBox="0 0 667 250">
      <defs><linearGradient id="ctaRed" x1="0" y1="0" x2="1" y2="1"><stop offset="0" stop-color="#7a1f18"/><stop offset=".5" stop-color="#9a3528"/><stop offset="1" stop-color="#6e1c16"/></linearGradient></defs>
      <path d="M0 30 C150 10 320 -5 420 10 C480 20 470 70 500 70 C550 70 620 30 667 0 L667 250 L0 250 Z" fill="url(#ctaRed)"/>
      <path d="M0 215 C150 175 320 160 440 165 C480 167 475 200 485 220 C495 238 530 236 570 220 C620 198 645 170 667 155 L667 250 L0 250 Z" fill="#232323"/>
      <path d="M0 215 C150 175 320 160 440 165 C480 167 475 200 485 220 C495 238 530 236 570 220 C620 198 645 170 667 155" fill="none" stroke="#0b5a8c" stroke-width="5"/>
    </svg>
    <h2>Sua família saudável.</h2>
    <a class="btn">AGENDE UMA CONSULTA</a>
  </section>

  <footer class="site-footer">
    <div class="f-brand">LUMERIA.NET</div>
    <p class="f-about">A história da Equipe de Cirurgia Vascular da Clinilab e Serrano Consultório Médico inicia-se com a História da Cirurgia Vascular do Brasil. O nosso logotipo também tem uma história muito legal. Estamos há mais de 3 décadas resolvendo problemas vasculares.</p>
    <div class="f-col" style="left:280px"><h3>Useful Links</h3><a href="https://lumeria.net/a-clinica/">A Clínica</a><a href="#">A Equipe</a><a href="#">Problemas Vasculares</a><a href="#">Soluções</a><a href="https://lumeria.net/contato/">Contato</a></div>
    <div class="f-col" style="left:391px"><h3>Importantes</h3><a href="#">Mapa e Endereço</a><a href="#">Sintomas Vasculares</a><a href="#">Lipedema</a></div>
    <div class="social"><span></span><span></span><span></span><span></span><span></span></div>
    <div class="f-rule"></div>
    <span class="to-top"></span>
    <p class="copy">Copyright © 2020. Sua equipe médica de confiança de Cirurgia Vascular em São Paulo, SP.</p>
  </footer>
</div>
</body>
</html>
```